Halvick Answering Service Brochure

Design a brochure for an answering service/call center based on the information submitted/attached. Photos and text will be included. Would like it designed to complement the logo provided. This brochure will explain to the potential customer who we are and what we have to offer.

The Halvick representatives take and processes inbound calls, 24-7-365

Target Market(s)

Any business, however, primarily Medical, oil and gas, non profits, and the service industry

Industry/Entity Type

Telecommunications

Font styles to use
Serif
Other font styles liked:
• coordinate with logo

Requirements
Must have
• Modern, bright, bold and neatly structured brochure that will complement the logo and our brand.

```html
<!DOCTYPE html>
<html lang="en">
<head>
<meta charset="utf-8">
<title>Halvick Answering Service Brochure</title>
<link href="https://fonts.googleapis.com/css2?family=Questrial&family=Arimo:wght@400;700&display=swap" rel="stylesheet">
<style>
:root{
  --bg:#a9a9a9;
  --paper:#ffffff;
  --red:#d3112a;
  --red-dark:#a80b1f;
  --charcoal:#2f2f2f;
  --ink:#1c1c1c;
  --photo-light:#eceae8;
  --photo-mid:#b9b3ad;
}
*{box-sizing:border-box;margin:0;padding:0}
html,body{width:1200px;height:978px;overflow:hidden;background:var(--bg)}
body{font-family:"Questrial",Arial,sans-serif;color:var(--ink);position:relative}
.page{position:absolute;top:136px;height:712px;background:var(--paper);overflow:hidden}
.page-left{left:125px;width:484px}
.page-right{left:609px;width:500px}
.swoosh{position:absolute;left:0;top:0}
.block{position:absolute;font-size:11px;line-height:13px}
.block p{text-align:justify;margin-bottom:8px}
.label{display:inline-block;background:var(--red);color:#fff;font-size:14.5px;line-height:17px;padding:2px 6px 2px 5px;border-radius:0 4px 4px 0;margin-bottom:8px}
.label.two-line{width:213px}
.ticks{list-style:none}
.ticks li{position:relative;padding-left:15px;margin-bottom:1px}
.ticks li::before{content:"\2713";position:absolute;left:0;top:0;color:var(--red);font-weight:bold}
.automated{font-size:10.5px}
.automated p{font-family:"Arimo",Arial,sans-serif;letter-spacing:-0.4px;line-height:12px;margin-bottom:6px}
.automated .label{margin-bottom:6px}
.automated .ticks li{margin-bottom:0;line-height:13px}
.subhead{font-family:"Arimo",Arial,sans-serif;font-weight:700;font-size:14px;border-bottom:1.5px solid var(--red);padding-bottom:1px;margin-bottom:4px}
.info-title{position:absolute;left:56px;top:664px;font-size:17px}
.info-url{position:absolute;left:28px;top:686px;width:184px;height:26px;background:var(--red);color:#fff;font-family:"Arimo",Arial,sans-serif;font-weight:700;font-size:14px;line-height:26px;padding-left:18px;border-radius:6px 0 0 0}
.industry-box{position:absolute;left:248px;top:208px;width:228px;height:165px;background:var(--charcoal);color:#fff;border-radius:12px;padding:14px 6px 0 6px;font-size:11px;line-height:13px;text-align:justify}
</style>
</head>
<body>

<section class="page page-left">
  <svg class="swoosh" width="484" height="330" viewBox="0 0 484 330">
    <defs>
      <linearGradient id="team" x1="0" y1="0" x2="1" y2="1">
        <stop offset="0" stop-color="#f4f2f0"/>
        <stop offset="0.5" stop-color="#b9b3ad"/>
        <stop offset="1" stop-color="#e2dfdc"/>
      </linearGradient>
    </defs>
    <path role="img" aria-label="Photo of a smiling customer service team wearing headsets" d="M0 0 H484 C430 120 300 250 0 270 Z" fill="url(#team)"/>
    <path d="M0 290 C300 268 440 150 484 4 V40 C440 190 300 300 0 312 Z" fill="var(--charcoal)"/>
    <path d="M0 300 C310 285 450 160 484 20 V70 C440 210 300 315 0 322 Z" fill="var(--red)"/>
  </svg>

  <div class="block" style="left:15px;top:331px;width:226px">
    <span class="label">About Us:</span>
    <p>Halvick, over the past 84 years, has operated through wars, floods and hurricanes. Our long history is important as it shows Consistency, Professionalism, Experience, and a Can Do Attitude, which is hard to find in the answering service industry today.</p>
    <p>At Halvick, you'll never be just another a number. We will become part of YOUR team on day one and remain there, ready and honored to serve by providing reliable, professional answering services, 24-7-365, as needed.</p>
    <span class="label">Still Growing? Find a Scalable<br>Phone Answering Service</span>
    <p>A scalable solution is one that doesn't waste resources when you don't need them, but easily adapts to future growth. All of our services at Halvick grow with you, meaning you don't pay for additional support until you need it.</p>
  </div>

  <div class="block" style="left:250px;top:272px;width:216px">
    <span class="label two-line">Automated or Live – Answering Services That Work for You</span>
    <p>Tell us about your needs and your budget and we'll do the rest. Halvick selects a system that satisfies your basic requirements, then evaluates your business to find a long-term solution that will work for you and your customers.</p>
    <span class="label">Live Answering Service</span>
    <p>Keystone Response is more than an answering service, it's an extension of your company. Our professional representatives take pride in being your direct line of communication with existing customers, potential customers and valued business partners. Before we start fielding calls, our representatives are trained according to the details of your business and industry.</p>
    <ul class="ticks">
      <li>24 Hour Answering Service</li>
      <li>Virtual Receptionist / Virtual Assistant</li>
      <li>Live Message Relay</li>
      <li>Help Desk Overflow</li>
      <li>Call Screening</li>
      <li>Bilingual Answering (Spanish Answering Service)</li>
      <li>Automated Services</li>
    </ul>
  </div>

  <div class="info-title">Any information:</div>
  <div class="info-url">www. Halvicksvc.com</div>
</section>

<section class="page page-right">
  <div class="block automated" style="left:16px;top:22px;width:224px">
    <span class="label">Automated Services</span>
    <p>Live answering services are not necessary for all businesses. Keystone Response offers automated answering services as a cost-effective option for continuous customer contact. And just because it's "automated" that doesn't mean it isn't tailored to the specific needs of your business.</p>
    <p>(Live and automated services can be combined for s very cost effective and professional solution.)</p>
    <p>Here are some of the customizable automated solutions we offer for businesses of all sizes:</p>
    <ul class="ticks">
      <li>Voice Mail (with or without extensions/sub-boxes)</li>
      <li>Voice Mail with Operator Revert</li>
      <li>Call Routing &amp; Transfer</li>
      <li>Web Integration</li>
      <li>Database Interaction</li>
      <li>Text Messaging</li>
      <li>Alpha Paging</li>
      <li>Email</li>
      <li>Fax</li>
      <li>Combination Service – Utilize our reliable voice mail system with an operator revert functionality. Your callers have the option of pressing "0" for a representative at any time.</li>
    </ul>
  </div>

  <div class="block" style="left:16px;top:406px;width:220px">
    <span class="label">Call Center Services Done Right</span>
    <p>Halvick is a complete call center provider. We train our representatives to follow your business protocol and then they are able to work as an autonomous unit that only requires your attention if you wish to change a procedure. Our call center representatives handle everything from pre-qualification to appointment setting and order taking. The Keystone Response team is your team.</p>
    <div class="subhead">Our call center services include:</div>
    <ul class="ticks">
      <li>Order Taking (on your site or our system)</li>
      <li>Pre-Qualification</li>
      <li>Help Desk</li>
      <li>Appointment Setting</li>
      <li>Appointment Confirmation</li>
      <li>Lead Generation</li>
      <li>Order Processing</li>
    </ul>
  </div>

  <div class="block" style="left:248px;top:22px;width:228px">
    <span class="label" style="width:170px">Special Services</span>
    <p>Medical Answering Services – Keystone Response representatives understand the unique needs of the medical community and are trained to provide the support you need.</p>
    <ul class="ticks" style="margin-top:14px">
      <li>HIPAA compliant messaging system</li>
      <li>Medical messages stored securely for 1 year</li>
      <li>Disaster Recovery – stay in contact with employees, management and customers in the event of emergency</li>
    </ul>
  </div>

  <div class="industry-box">
    Oil and Gas – We serve many clients in the Energy industry and our representatives are well-versed in handling customer relations in what can be a demanding field.<br>
    Commercial Property Management – Our representatives have experience maintaining positive relations with tenants, property managers and other real estate personnel.<br>
    *Ask one of our representatives about custom solutions for your industry
  </div>

  <div class="block" style="left:256px;top:406px;width:220px">
    <span class="label" style="width:132px">Test Drive</span>
    <p style="text-align:left">There's no better way to get a feel for our services than by speaking with one of our own representatives – 866.555.0190.</p>
  </div>

  <svg class="swoosh" style="top:512px" width="500" height="200" viewBox="0 0 500 200">
    <defs>
      <linearGradient id="agents" x1="0" y1="0" x2="1" y2="0">
        <stop offset="0" stop-color="#f1eeec"/>
        <stop offset="0.5" stop-color="#c9bfb6"/>
        <stop offset="1" stop-color="#9aa3ad"/>
      </linearGradient>
    </defs>
    <path d="M180 200 C230 110 360 40 500 30 V42 C370 55 250 120 196 200 Z" fill="var(--red)"/>
    <path role="img" aria-label="Photo of call center agents wearing headsets at work" d="M200 200 C255 125 370 60 500 48 V200 Z" fill="url(#agents)"/>
  </svg>
</section>

</body>
</html>
```